BPR Business Card

We need a business card that reflect our business, we have put anther business card as an example of what we like but please feel free to do your own thing.

Here are the items to be placed on card

Glen Harwick
Bright Parcel Route
Mobile: 917-555-4862
Office: 516-555-7104
Fax: 866-555-3927
Email: info@brightparcelroute.example
Website: brightparcelroute.example

I have added raw files to upload

Glen Harwick
Bright Parcel Route
Mobile: 917-555-4862
Office: 516-555-7104
Fax: 866-555-3927 

Target Market(s)

Natural product manufactures, and retailers and distributors

Industry/Entity Type

Business

Requirements
Must have
• 1. Logo
2. The colors of the company

```html
<!DOCTYPE html>
<html lang="en">
<head>
<meta charset="utf-8">
<title>Bright Parcel Route – Business Card</title>
<link rel="stylesheet" href="https://fonts.googleapis.com/css2?family=Antonio:wght@700&family=Oswald:wght@700&family=Roboto+Condensed:wght@300&display=swap">
<style>
  :root {
    --paper: #ffffff;
    --brand-green: #6cb644;
    --ink-dark: #2b2b2b;
    --ink-black: #111111;
    --crop-line: #000000;
  }
  html, body {
    margin: 0;
    padding: 0;
    width: 1200px;
    height: 792px;
    overflow: hidden;
    background: var(--paper);
  }
  .card {
    position: relative;
    width: 1200px;
    height: 792px;
    background: var(--paper);
  }
  .crop-marks {
    position: absolute;
    inset: 0;
  }
  .brand {
    position: absolute;
    left: 240px;
    top: 236px;
    width: 697px;
    height: 220px;
    display: flex;
    align-items: center;
    justify-content: center;
    gap: 26px;
  }
  .brand-square {
    width: 150px;
    height: 150px;
    background: var(--brand-green);
    flex: none;
  }
  .brand-name {
    margin: 0;
    font-family: "Oswald", "Arial Narrow", sans-serif;
    font-weight: 700;
    font-size: 76px;
    line-height: 0.98;
    text-transform: uppercase;
    color: var(--brand-green);
    white-space: nowrap;
  }
  .brand-name span { display: block; }
  .person-name {
    position: absolute;
    left: 0;
    right: 0;
    top: 452px;
    margin: 0;
    text-align: center;
    font-family: "Antonio", "Oswald", "Arial Narrow", sans-serif;
    font-weight: 700;
    font-size: 110px;
    line-height: 1.05;
    letter-spacing: -1px;
    color: var(--ink-dark);
  }
  .contact {
    position: absolute;
    top: 590px;
    margin: 0;
    font-family: "Roboto Condensed", "Arial Narrow", sans-serif;
    font-weight: 300;
    font-size: 34px;
    line-height: 1.2;
    color: var(--ink-black);
    white-space: nowrap;
  }
  .contact-label { margin-right: 12px; }
  .contact--mobile { left: 226px; }
  .contact--office { left: 720px; }
  .contact-extra {
    position: absolute;
    left: 0;
    right: 0;
    top: 636px;
    margin: 0;
    display: flex;
    justify-content: center;
    gap: 34px;
    font-family: "Roboto Condensed", "Arial Narrow", sans-serif;
    font-weight: 300;
    font-size: 19px;
    line-height: 1.2;
    color: var(--ink-black);
    white-space: nowrap;
  }
</style>
</head>
<body>
  <main class="card">
    <svg class="crop-marks" width="1200" height="792" viewBox="0 0 1200 792" aria-hidden="true">
      <g stroke="var(--crop-line)" stroke-width="1.2">
        <line x1="124" y1="0" x2="124" y2="100"/>
        <line x1="1075" y1="0" x2="1075" y2="100"/>
        <line x1="124" y1="690" x2="124" y2="792"/>
        <line x1="1075" y1="690" x2="1075" y2="792"/>
        <line x1="0" y1="124" x2="100" y2="124"/>
        <line x1="1097" y1="124" x2="1200" y2="124"/>
        <line x1="0" y1="667" x2="100" y2="667"/>
        <line x1="1097" y1="667" x2="1200" y2="667"/>
      </g>
    </svg>

    <div class="brand">
      <span class="brand-square" aria-hidden="true"></span>
      <h1 class="brand-name"><span>Bright Parcel</span><span>Route</span></h1>
    </div>

    <p class="person-name">Glen Harwick</p>

    <p class="contact contact--mobile"><span class="contact-label">M</span>917-555-4862</p>
    <p class="contact contact--office"><span class="contact-label">O</span>516-555-7104</p>

    <p class="contact-extra">
      <span class="contact-fax">F 866-555-3927</span>
      <span class="contact-email">info@brightparcelroute.example</span>
      <span class="contact-web">brightparcelroute.example</span>
    </p>
  </main>
</body>
</html>
```